Business Card Design Project

I need the business card designed with my current logo. I would like to have Arabic text as well in the logo, saying qasr al yasmin.

```html
<!DOCTYPE html>
<html lang="en">
<head>
<meta charset="utf-8">
<title>qasr al yasmin – business card</title>
<link href="https://fonts.googleapis.com/css2?family=Comfortaa:wght@500;700&family=Share+Tech&display=swap" rel="stylesheet">
<style>
  :root {
    --backdrop: #3b3836;
    --card-dark: #070c08;
    --card-light: #f4f6f3;
    --green: #4f9a3a;
    --green-bright: #5cc23f;
    --green-deep: #2f5e2a;
    --ink: #1e1f1e;
    --ink-soft: #555a55;
  }
  * { margin: 0; padding: 0; box-sizing: border-box; }
  html, body { width: 1200px; height: 642px; overflow: hidden; }
  body {
    background: var(--backdrop);
    position: relative;
    font-family: "Share Tech", "Arial Narrow", sans-serif;
  }
  .card {
    position: absolute;
    width: 540px;
    height: 310px;
    overflow: hidden;
    box-shadow: 0 10px 24px rgba(0,0,0,.45);
  }

  /* Front */
  .card--front {
    left: 40px; top: 50px;
    background: var(--card-dark);
  }
  .front__glow {
    position: absolute; inset: 0;
    background:
      radial-gradient(ellipse 42% 55% at 48% 40%, rgba(76,170,52,.35), transparent 70%),
      linear-gradient(180deg, #0b1a0d 0%, #071008 60%, #050805 100%);
  }
  .front__brand {
    position: absolute; left: 0; right: 0; top: 118px;
    display: flex; align-items: center; justify-content: center; gap: 14px;
  }
  .brand-dot {
    width: 22px; height: 22px; border-radius: 50%;
    background: var(--green-bright);
  }
  .front__name {
    font-family: "Comfortaa", sans-serif; font-weight: 700;
    font-size: 50px; color: var(--green-bright); letter-spacing: .5px;
  }
  .front__web {
    position: absolute; left: 0; right: 0; top: 232px;
    text-align: center; font-size: 15px; letter-spacing: 1.5px;
    color: var(--green-bright);
  }

  /* Back */
  .card--back {
    left: 620px; top: 282px;
    background: var(--card-light);
  }
  .back__brand {
    position: absolute; left: 0; right: 0; top: 46px;
    display: flex; align-items: center; justify-content: center; gap: 12px;
  }
  .back__brand .brand-dot { background: var(--green); width: 18px; height: 18px; }
  .back__name {
    font-family: "Comfortaa", sans-serif; font-weight: 700;
    font-size: 38px; color: var(--ink);
  }
  .person {
    position: absolute; right: 26px; top: 118px; text-align: right;
  }
  .person__name {
    font-family: "Comfortaa", sans-serif; font-weight: 700;
    font-size: 21px; color: var(--ink);
  }
  .person__role { font-size: 12px; color: var(--green); margin-top: 4px; }
  .person__cell { font-size: 12px; color: var(--ink); }
  .contact {
    position: absolute; left: 30px; top: 170px;
    font-size: 13px; color: var(--ink-soft); line-height: 16px;
  }
  .contact__row { display: flex; align-items: center; gap: 8px; }
  .contact__row svg { width: 16px; height: 12px; }
  .contact__gap { margin-left: 30px; }
  .back__skyline {
    position: absolute; left: 0; right: 0; top: 220px; height: 52px;
    background: linear-gradient(180deg, rgba(200,210,200,0) 0%, rgba(190,200,190,.55) 100%);
  }
  .back__rule { position: absolute; left: 0; right: 0; height: 2px; background: var(--green-deep); }
  .back__web {
    position: absolute; right: 36px; top: 273px;
    font-size: 11px; letter-spacing: .8px; color: var(--ink);
  }
  .back__base {
    position: absolute; left: 0; right: 0; bottom: 0; height: 18px;
    background: linear-gradient(180deg, var(--card-light) 0 4px, var(--green-deep) 4px 7px, #e6ebe4 7px 11px, var(--green) 11px 13px, #eef1ec 13px);
  }
</style>
</head>
<body>

<section class="card card--front">
  <div class="front__glow" role="img" aria-label="Soft green glow on a dark green background"></div>
  <div class="front__brand">
    <span class="brand-dot"></span>
    <span class="front__name">qasr al yasmin</span>
  </div>
  <p class="front__web">www.qasralyasmin.com</p>
</section>

<section class="card card--back">
  <div class="back__brand">
    <span class="brand-dot"></span>
    <span class="back__name">qasr al yasmin</span>
  </div>

  <div class="person">
    <p class="person__name">Name Lastname</p>
    <p class="person__role">General Manager</p>
    <p class="person__cell">Cell.000-000-0000</p>
  </div>

  <div class="contact">
    <p>123 streetname</p>
    <p>city,country 99999</p>
    <p class="contact__row">
      <svg viewBox="0 0 16 12"><path d="M2 4 Q8 0 14 4 L12 6 L10 5 L10 4 L6 4 L6 5 L4 6 Z M4 7 H12 L13 11 H3 Z" fill="#3a7a2e"/></svg>
      000-000-0000
      <svg class="contact__gap" viewBox="0 0 16 12"><rect x="1" y="2" width="14" height="9" fill="none" stroke="#3a7a2e" stroke-width="1.5"/><rect x="4" y="0.5" width="8" height="3" fill="#3a7a2e"/></svg>
      000-000-0000
    </p>
    <p class="contact__row">
      <svg viewBox="0 0 16 12"><rect x="1" y="1" width="14" height="10" fill="none" stroke="#3a7a2e" stroke-width="1.5"/><path d="M1 1 L8 7 L15 1" fill="none" stroke="#3a7a2e" stroke-width="1.5"/></svg>
      name@qasralyasmin.com
    </p>
  </div>

  <div class="back__skyline" role="img" aria-label="Faint grey skyline decoration along the lower edge"></div>
  <div class="back__rule" style="top:270px"></div>
  <p class="back__web">www.qasralyasmin.com</p>
  <div class="back__base"></div>
</section>

</body>
</html>
```